Bref créative
Trucking Company Business Cards Stationary
KVR Freight Solutions
Professional
Beto Quiroga
Terminal Manager
4100 Harborview Blvd
Marlow Bay, TX 77500
kvrfreightsolutions@mailbox-example.com
i would like something similar to this on the back side of card
i would also like something similar to this on the back side of my card

```html
<!DOCTYPE html>
<html lang="en">
<head>
<meta charset="utf-8">
<title>KVR Freight Solutions — Business Cards</title>
<link href="https://fonts.googleapis.com/css2?family=Open+Sans:wght@400;600;700&display=swap" rel="stylesheet">
<style>
  :root {
    --brand-red: #c8161d;
    --brand-red-dark: #9e0f15;
    --steel: #b9bcc0;
    --steel-light: #e3e4e6;
    --ink: #4a4a4a;
    --paper: #ffffff;
    --backdrop: #d6d7d9;
  }
  * { box-sizing: border-box; margin: 0; padding: 0; }
  html, body {
    width: 1200px; height: 895px; overflow: hidden;
    background: var(--backdrop);
    font-family: "Open Sans", Arial, sans-serif;
  }
  .sheet {
    width: 1200px; height: 895px;
    display: flex; flex-direction: column;
    align-items: center; justify-content: center; gap: 46px;
  }
  .card {
    position: relative;
    width: 660px; height: 377px;
    background: var(--paper);
    box-shadow: 0 6px 18px rgba(0,0,0,0.18);
    overflow: hidden;
  }
  .brand-name {
    font-weight: 700;
    color: var(--brand-red);
    letter-spacing: 0.5px;
    display: flex; align-items: center; gap: 12px;
    white-space: nowrap;
  }
  .brand-dot {
    width: 16px; height: 16px; border-radius: 50%;
    background: var(--brand-red);
  }
  /* Front card */
  .card--front {
    display: flex; flex-direction: column;
    align-items: center; justify-content: center; gap: 38px;
  }
  .card--front .brand-name { font-size: 40px; }
  .website {
    font-size: 21px; color: var(--ink);
    letter-spacing: 3px;
  }
  /* Back card */
  .card--back .waves { position: absolute; inset: 0; }
  .card--back .brand-name {
    position: absolute; top: 48px; left: 0; right: 0;
    justify-content: center; font-size: 30px;
  }
  .details {
    position: absolute; left: 0; right: 0; top: 222px;
    display: flex; justify-content: center; gap: 26px;
    color: var(--paper);
  }
  .person {
    text-align: right; font-size: 13px; line-height: 1.55;
    padding-right: 26px;
    border-right: 1px solid rgba(255,255,255,0.7);
    white-space: nowrap;
  }
  .person-name { font-weight: 700; font-size: 16px; }
  .person-role { font-weight: 600; margin-bottom: 6px; }
  .contact-list { list-style: none; font-size: 12.5px; line-height: 1.75; white-space: nowrap; }
  .contact-list li { display: flex; align-items: center; gap: 8px; }
  .contact-icon { width: 15px; height: 15px; flex: none; }
</style>
</head>
<body>
<main class="sheet">

  <section class="card card--front" aria-label="Card front">
    <div class="brand-name"><span class="brand-dot"></span>KVR Freight Solutions</div>
    <p class="website">www.kvrfreight-example.com</p>
  </section>

  <section class="card card--back" aria-label="Card back">
    <svg class="waves" viewBox="0 0 660 377" preserveAspectRatio="none" aria-hidden="true">
      <defs>
        <linearGradient id="steelBand" x1="0" y1="0" x2="1" y2="0">
          <stop offset="0" stop-color="#e3e4e6"/>
          <stop offset="0.5" stop-color="#b9bcc0"/>
          <stop offset="1" stop-color="#e3e4e6"/>
        </linearGradient>
        <linearGradient id="redField" x1="0" y1="0" x2="0" y2="1">
          <stop offset="0" stop-color="#c8161d"/>
          <stop offset="1" stop-color="#9e0f15"/>
        </linearGradient>
      </defs>
      <path d="M0,150 C180,118 420,178 660,118 L660,377 L0,377 Z" fill="url(#steelBand)"/>
      <path d="M0,168 C200,140 430,190 660,140 L660,377 L0,377 Z" fill="#ffffff"/>
      <path d="M0,178 C210,152 430,198 660,150 L660,377 L0,377 Z" fill="url(#redField)"/>
    </svg>

    <div class="brand-name"><span class="brand-dot"></span>KVR Freight Solutions</div>

    <div class="details">
      <div class="person">
        <p class="person-name">Beto Quiroga</p>
        <p class="person-role">Terminal Manager</p>
        <p>4100 Harborview Blvd</p>
        <p>Marlow Bay, TX 77500</p>
      </div>
      <ul class="contact-list">
        <li>
          <svg class="contact-icon" viewBox="0 0 16 16" aria-hidden="true"><circle cx="8" cy="8" r="8" fill="#fff"/><path d="M5.2 4.2l1.4-.4 1 2.1-.9.8c.4.9 1.1 1.6 2 2l.8-.9 2.1 1-.4 1.4c-3.4.3-6.3-2.6-6-6z" fill="#c8161d"/></svg>
          (281) 555-0147
        </li>
        <li>
          <svg class="contact-icon" viewBox="0 0 16 16" aria-hidden="true"><circle cx="8" cy="8" r="8" fill="#fff"/><path d="M5.2 4.2l1.4-.4 1 2.1-.9.8c.4.9 1.1 1.6 2 2l.8-.9 2.1 1-.4 1.4c-3.4.3-6.3-2.6-6-6z" fill="#c8161d"/></svg>
          (281) 555-0193
        </li>
        <li>
          <svg class="contact-icon" viewBox="0 0 16 16" aria-hidden="true"><circle cx="8" cy="8" r="8" fill="#fff"/><rect x="4" y="5" width="8" height="6" fill="none" stroke="#c8161d" stroke-width="1.2"/><path d="M4 5l4 3.4L12 5" fill="none" stroke="#c8161d" stroke-width="1.2"/></svg>
          kvrfreightsolutions@mailbox-example.com
        </li>
        <li>
          <svg class="contact-icon" viewBox="0 0 16 16" aria-hidden="true"><circle cx="8" cy="8" r="8" fill="#fff"/><circle cx="8" cy="8" r="4.2" fill="none" stroke="#c8161d" stroke-width="1.1"/><path d="M3.8 8h8.4M8 3.8c-2 2.4-2 6 0 8.4M8 3.8c2 2.4 2 6 0 8.4" fill="none" stroke="#c8161d" stroke-width="1"/></svg>
          kvrfreight-example.com
        </li>
      </ul>
    </div>
  </section>

</main>
</body>
</html>
```